K & D A/C Compressors' Business Card

Hello,

I need someone to create a new business card for my business. The name of my Business is: K & D A/C Compressors. I sell automotive air conditioning parts (a/c parts). I would like the business card to incorporate my logo, and to have an automotive feel to it. It is important that the business card feel like it is coming from an automotive parts business.

I already have a logo, which I will provide.

Thanks.
Updates

Project Deadline Extended Reason: I feel like extending the deadline until October 9, 2017, will allow for more time to design the business card. Thank you for your understanding. Added Monday, October 2, 2017

Target Market(s)

Consumers who need automotive a/c parts, and auto mechanics.

Industry/Entity Type

Automotive

Contact Information for Business Card

Business name: K & D A/C Compressors
Business Address: 48207 Southwest 36th Street, Palm Crest, Florida 33471
Telephone: 305-472-1390
Fax: To be provided once I choose your design.
Website: www.kdcoolunits.example
Email: support@kdcoolunits.example
Names: To be provided once I choose your design.

Font styles to use
Sans Serif

Colors

Designer to choose colors to be used in the design.

Requirements
Must have
• The business card must include all of the "Business Card Details" and the logo I have uploaded.

```html
<!DOCTYPE html>
<html lang="en">
<head>
<meta charset="utf-8">
<title>K &amp; D A/C Compressors – Business Card</title>
<link rel="stylesheet" href="https://fonts.googleapis.com/css2?family=Poppins:wght@200;300&family=Marcellus&display=swap">
<style>
  :root {
    --page: #ffffff;
    --frame: #222222;
    --card-edge: #060606;
    --card-mid: #454545;
    --text-white: #ffffff;
    --text-grey: #a7a8aa;
    --accent: #17a6e6;
    --metal-light: #d4d4d4;
    --metal-dark: #6e6e6e;
    --icon-bg: #e2e2e2;
    --icon-ink: #2a2a2a;
  }
  * { box-sizing: border-box; margin: 0; padding: 0; }
  html, body { width: 1200px; height: 1200px; overflow: hidden; background: var(--page); }
  .canvas {
    position: relative; width: 1200px; height: 1200px;
    border: 1px solid var(--frame);
  }
  .card {
    position: absolute; left: 180px; width: 840px; height: 481px;
    background: linear-gradient(90deg, var(--card-edge) 0%, #2b2b2b 25%, var(--card-mid) 55%, #2f2f2f 80%, var(--card-edge) 100%);
    overflow: hidden;
    font-family: "Poppins", sans-serif;
  }
  .card--front { top: 90px; }
  .card--back { top: 630px; }

  .brand { position: absolute; color: var(--text-grey); font-weight: 300; line-height: 1; }
  .brand__row { display: flex; align-items: center; gap: 16px; }
  .brand__mark { width: 24px; height: 24px; background: var(--accent); flex: none; }
  .brand__big { font-size: 60px; letter-spacing: 2px; white-space: nowrap; }
  .brand__small { display: block; font-size: 32px; margin-top: 10px; white-space: nowrap; }
  .card--front .brand { left: 76px; top: 118px; }
  .card--back .brand { left: 538px; top: 58px; }
  .card--back .brand__big { font-size: 50px; }
  .card--back .brand__small { font-size: 28px; margin-top: 8px; }

  .person { position: absolute; color: var(--text-white); font-weight: 200; }
  .person__name { display: block; font-size: 62px; line-height: 1; }
  .person__role { display: block; font-size: 24px; letter-spacing: 17px; margin-top: 4px; line-height: 1; color: var(--text-white); }
  .card--front .person { left: 124px; top: 288px; }
  .card--back .person { left: 60px; top: 46px; }

  .art {
    position: absolute; left: 460px; top: 166px; width: 348px; height: 315px;
    background: linear-gradient(135deg, var(--metal-light) 0%, var(--metal-dark) 100%);
    opacity: 0.55;
    border-radius: 40px 40px 0 0;
  }

  .contact {
    position: absolute; left: 60px; top: 184px;
    font-family: "Marcellus", serif; color: var(--text-white);
  }
  .contact__address { font-size: 21px; line-height: 32px; }
  .contact__list { list-style: none; margin-top: 14px; }
  .contact__item { display: flex; align-items: center; gap: 20px; height: 46px; font-size: 21px; }
  .contact__icon {
    width: 28px; height: 28px; border-radius: 50%; background: var(--icon-bg);
    display: flex; align-items: center; justify-content: center; flex: none;
  }
  .contact__icon svg { width: 16px; height: 16px; }
</style>
</head>
<body>
<div class="canvas">

  <section class="card card--front">
    <div class="brand">
      <div class="brand__row"><span class="brand__mark"></span><span class="brand__big">K &amp; D</span></div>
      <span class="brand__small">A/C Compressors</span>
    </div>
    <div class="person">
      <span class="person__name">Names</span>
      <span class="person__role">Position</span>
    </div>
    <div class="art" role="img" aria-label="Metallic illustration of a fist gripping a wrench"></div>
  </section>

  <section class="card card--back">
    <div class="person">
      <span class="person__name">Names</span>
      <span class="person__role">Position</span>
    </div>
    <div class="brand">
      <div class="brand__row"><span class="brand__mark"></span><span class="brand__big">K &amp; D</span></div>
      <span class="brand__small">A/C Compressors</span>
    </div>
    <div class="contact">
      <p class="contact__address">48207 Southwest 36th Street,<br>Palm Crest, Florida 33471</p>
      <ul class="contact__list">
        <li class="contact__item">
          <span class="contact__icon"><svg viewBox="0 0 16 16"><rect x="2" y="5" width="12" height="9" rx="1" fill="none" stroke="#2a2a2a" stroke-width="1.4"/><rect x="4" y="2" width="6" height="4" fill="none" stroke="#2a2a2a" stroke-width="1.2"/><rect x="8" y="8" width="4" height="3" fill="#2a2a2a"/></svg></span>
          <span>xxxxxxxxxxx</span>
        </li>
        <li class="contact__item">
          <span class="contact__icon"><svg viewBox="0 0 16 16"><path d="M4 2 L6.5 2 L7.5 5 L6 6.5 Q7.5 9.5 9.5 10 L11 8.5 L14 9.5 L14 12 Q13 14 11 14 Q3 12 2 4 Q2 2 4 2 Z" fill="none" stroke="#2a2a2a" stroke-width="1.2"/></svg></span>
          <span>305-472-1390</span>
        </li>
        <li class="contact__item">
          <span class="contact__icon"><svg viewBox="0 0 16 16"><rect x="2" y="4" width="12" height="9" fill="none" stroke="#2a2a2a" stroke-width="1.3"/><path d="M2 4 L8 9 L14 4" fill="none" stroke="#2a2a2a" stroke-width="1.3"/></svg></span>
          <span>support@kdcoolunits.example</span>
        </li>
        <li class="contact__item">
          <span class="contact__icon"><svg viewBox="0 0 16 16"><circle cx="8" cy="8" r="6" fill="none" stroke="#2a2a2a" stroke-width="1.3"/><ellipse cx="8" cy="8" rx="2.6" ry="6" fill="none" stroke="#2a2a2a" stroke-width="1.1"/><path d="M2 8 H14" stroke="#2a2a2a" stroke-width="1.1"/></svg></span>
          <span>www.kdcoolunits.example</span>
        </li>
      </ul>
    </div>
    <div class="art" role="img" aria-label="Metallic illustration of a fist gripping a wrench"></div>
  </section>

</div>
</body>
</html>
```